Design Business Card & Electronic Word Document Stationary

Hi thanks for playing business card design wheel of fortune with me. :D

Please see the attached Word doc with very detailed instructions on this double-sided 2 or 3 color business card design with matching Microsoft Word online stationary design (letterhead and fax cover sheet).

All the business card content and colors to use are provided in the specs, the color and layout of the design is the only thing you're collarborating with me on doing with this contest project please note. I also provided a couple dozen modern business card examples in the specs as well, to better help your odds on winning the bid to put you on the right path on what I'm looking for design wise.

Thanks so much and good luck to you.

```html
<!DOCTYPE html>
<html lang="en">
<head>
<meta charset="utf-8">
<title>Roam Wrench Business Card</title>
<link href="https://fonts.googleapis.com/css2?family=Open+Sans:ital,wght@0,300;0,400;0,600;0,700;1,400&display=swap" rel="stylesheet">
<style>
  :root {
    --page: #e9ebee;
    --card: #ffffff;
    --blue: #1f6ea6;
    --blue-light: #3a8ccc;
    --ink: #2b2b2b;
    --grey: #8a8f94;
    --dark-bar: #232323;
  }
  * { box-sizing: border-box; margin: 0; padding: 0; }
  html, body {
    width: 1200px; height: 900px; overflow: hidden;
    background: var(--page);
    font-family: "Open Sans", Arial, sans-serif;
    color: var(--ink);
  }
  .card {
    position: absolute; left: 240px;
    width: 720px; height: 411px;
    background: var(--card);
    border-radius: 18px;
    overflow: hidden;
    box-shadow: 0 4px 14px rgba(0,0,0,.12);
  }
  .card--front { top: 30px; }
  .card--back { top: 459px; }
  .swoosh { position: absolute; left: 0; top: 0; }

  /* Front */
  .dark-bar {
    position: absolute; left: 70px; top: 0;
    width: 58px; height: 150px;
    background: var(--dark-bar);
    border-radius: 0 0 8px 8px;
  }
  .brand-mark {
    position: absolute; left: 58px; top: 160px;
    display: flex; align-items: center; gap: 6px;
    font-size: 13px; font-weight: 700; color: var(--blue);
  }
  .brand-mark .dot {
    width: 14px; height: 14px; border-radius: 50%; background: var(--blue);
  }
  .person { position: absolute; left: 58px; top: 190px; width: 325px; }
  .person__name { font-size: 34px; line-height: 1; color: var(--blue-light); font-weight: 300; letter-spacing: .5px; }
  .person__name b { font-weight: 700; color: var(--blue); }
  .person__role { font-size: 12px; color: var(--grey); margin-top: 6px; letter-spacing: 1px; }
  .person__tagline { font-size: 11px; color: var(--ink); margin-top: 10px; white-space: nowrap; }

  .contacts { position: absolute; left: 400px; top: 140px; list-style: none; }
  .contacts li {
    display: flex; align-items: center; gap: 10px;
    font-size: 14px; font-weight: 600; color: var(--blue);
    height: 26px;
  }
  .contacts .icon {
    width: 18px; height: 18px; border-radius: 3px; background: var(--blue);
    display: flex; align-items: center; justify-content: center;
    flex: none;
  }

  /* Back */
  .back-brand {
    position: absolute; left: 28px; top: 22px;
    display: flex; align-items: center; gap: 6px;
    font-size: 13px; font-weight: 700; color: var(--blue);
  }
  .back-brand .dot { width: 14px; height: 14px; border-radius: 50%; background: var(--blue); }
  .intro {
    position: absolute; left: 220px; top: 22px; width: 460px;
    font-size: 13px; font-style: italic; color: var(--grey); line-height: 1.45;
  }
  .service { position: absolute; }
  .service h2 { font-size: 16px; font-weight: 400; color: var(--blue); margin-bottom: 5px; }
  .service p { font-size: 11px; line-height: 1.45; color: var(--ink); }
  .service--custom { left: 190px; top: 92px; width: 300px; }
  .service--range { right: 80px; top: 180px; width: 330px; text-align: right; }
  .service--mobile { right: 80px; top: 270px; width: 360px; text-align: right; }
  .badge {
    position: absolute; width: 30px; height: 30px; border-radius: 50%;
    background: linear-gradient(#5c6470, #2b3038);
  }
  .badge--custom { left: 150px; top: 92px; width: 30px; height: 20px; border-radius: 6px; background: linear-gradient(#3a4a8c,#1d2a5e); }
  .badge--range { right: 36px; top: 215px; }
  .badge--mobile { right: 36px; top: 300px; border-radius: 6px; background: linear-gradient(#8aa7c7,#3b5f8c); }
</style>
</head>
<body>

<section class="card card--front">
  <svg class="swoosh" width="720" height="411" viewBox="0 0 720 411" aria-hidden="true">
    <path d="M520 411 Q660 395 720 300 L720 411 Z" fill="var(--blue)"/>
  </svg>
  <div class="dark-bar"></div>
  <div class="brand-mark"><span class="dot"></span>Roam Wrench</div>
  <div class="person">
    <h1 class="person__name"><b>COLE</b> HARMON</h1>
    <p class="person__role">OWNER</p>
    <p class="person__tagline">Nationwide Mobile Mechanic &amp; Vehicle Customization Expert</p>
  </div>
  <ul class="contacts">
    <li><span class="icon"><svg width="10" height="10" viewBox="0 0 10 10"><path d="M2 1 L4 1 L4.6 3 L3.4 4 Q4.5 6 6 6.6 L7 5.4 L9 6 L9 8 Q5 9 2 6 Q1 4 2 1Z" fill="#fff"/></svg></span>555-014-2290</li>
    <li><span class="icon"><svg width="10" height="8" viewBox="0 0 10 8"><rect x=".5" y=".5" width="9" height="7" fill="none" stroke="#fff"/><path d="M.5 .5 L5 4.5 L9.5 .5" fill="none" stroke="#fff"/></svg></span>cole@roamwrench.com</li>
    <li><span class="icon"><svg width="10" height="10" viewBox="0 0 10 10"><circle cx="5" cy="5" r="4" fill="none" stroke="#fff"/><path d="M1 5 H9 M5 1 V9" stroke="#fff"/></svg></span>www.roamwrench.com</li>
    <li><span class="icon"></span>www.chirpline.com/roamwrench</li>
    <li><span class="icon"></span>www.clipcast.com/roamwrench</li>
    <li><span class="icon"></span>www.pinboardia.com/roamwrench</li>
    <li><span class="icon"></span>www.friendlyface.com/roamwrench</li>
  </ul>
</section>

<section class="card card--back">
  <svg class="swoosh" width="720" height="411" viewBox="0 0 720 411" aria-hidden="true">
    <path d="M0 40 Q150 80 190 240 Q110 130 0 120 Z" fill="var(--blue)"/>
  </svg>
  <div class="back-brand"><span class="dot"></span>Roam Wrench</div>
  <p class="intro">Free estimate and vehicle consultation! I will travel to you 7 days a week, day or night, for 50-75% less than what dealerships and shops will charge you.</p>

  <span class="badge badge--custom" role="img" aria-label="Small car illustration"></span>
  <div class="service service--custom">
    <h2>Vehicle Customization Services</h2>
    <p>I can install and customize lighting, audio, lift kits, wheels, hitches, racks and interior trim on most cars and trucks. Ask me about custom builds and upgrades.</p>
  </div>

  <span class="badge badge--range" role="img" aria-label="Tire illustration"></span>
  <div class="service service--range">
    <h2>What I can work on</h2>
    <p>I've worked on everything from fire trucks, tractors, food and catering trailers, buses, RV's, luxury, domestic and foreign vehicles, classic hot rods and muscle cars.</p>
  </div>

  <span class="badge badge--mobile" role="img" aria-label="Mechanic at work illustration"></span>
  <div class="service service--mobile">
    <h2>Mobile Mechanic Services</h2>
    <p>I can install and repair anything in your vehicles starting, charging, heating and cooling, fuel, engine, suspension, steering and transmission systems. I can replace any type of belts, hoses, filters, fluids, switches, sensors, relays, fuses or wiring. Sorry I don't do transmission or engine rebuilds or replacements.</p>
  </div>
</section>

</body>
</html>
```